Brochure Design Project

11x17 flat...folds to 8.5x11
full color
Utilize customers images and web content to create sleek brochure showcasing customers capabilities.
www.brightvaleworks.com
Logo added to uploads.
Reason: Customer is out of town.

```html
<!DOCTYPE html>
<html lang="en">
<head>
<meta charset="utf-8">
<title>Brightvale Works Brochure Spread</title>
<link rel="stylesheet" href="https://fonts.googleapis.com/css2?family=Open+Sans:wght@400;600;700&family=Cinzel:wght@600;700&family=Roboto+Condensed:wght@400&display=swap">
<style>
  :root {
    --stripe-bg: #e4e4e8;
    --purple: #8e4fa6;
    --violet: #5b4ea8;
    --teal: #1b93ad;
    --ink: #2b2b2b;
    --frame: #3aa6c4;
    --sheet-frame: #9fd3e6;
    --lime: #a6d14a;
    --white: #ffffff;
  }
  * { margin: 0; padding: 0; box-sizing: border-box; }
  html, body { width: 1200px; height: 776px; overflow: hidden; background: #fff; }
  .spread { position: relative; width: 1200px; height: 776px; overflow: hidden; font-family: "Open Sans", Arial, sans-serif; }
  .backdrop, .collage { position: absolute; left: 0; top: 0; }
  .banner-title {
    position: absolute; left: 88px; top: 68px;
    color: var(--white); font-weight: 700; font-size: 16.5px; line-height: 21px;
  }
  .product-sheet {
    position: absolute; top: 113px; width: 212px; height: 282px;
    background: var(--white); border: 2px solid var(--sheet-frame);
    display: grid; grid-template-columns: 1fr 1fr; grid-template-rows: 1fr 1fr;
    gap: 4px; padding: 6px 5px 5px;
  }
  .sheet-a { left: 88px; }
  .sheet-b { left: 302px; }
  .sheet-section { display: flex; flex-direction: column; }
  .section-bar {
    background: var(--lime); color: #3b4a14; font-size: 5.5px; font-weight: 700;
    height: 9px; line-height: 9px; padding: 0 3px; white-space: nowrap; overflow: hidden;
  }
  .section-photos { flex: 1; margin-top: 4px; border-radius: 2px; }
  .tone-pink { background: linear-gradient(150deg, #e84fa0, #5ec8e6 45%, #8fd14f 75%, #2d2d2d); }
  .tone-blue { background: linear-gradient(160deg, #3a3a44, #e85fa6 35%, #54c2e4 65%, #a6d14a); }
  .tone-lime { background: linear-gradient(150deg, #f4a23a, #e84fa0 40%, #3ab0dc 70%, #9bd14a); }
  .tone-mix { background: linear-gradient(160deg, #8fd14f, #e84fa0 45%, #2f2f38 70%, #54c2e4); }
  .caption {
    position: absolute; left: 88px; top: 403px; width: 290px;
    font-size: 8.3px; line-height: 11px; color: var(--ink);
  }
  .contact-card {
    position: absolute; left: 152px; top: 461px; width: 296px; height: 283px;
    background: var(--white); border: 1.5px solid var(--frame);
  }
  .brand-name {
    font-family: "Cinzel", Georgia, serif; font-weight: 700; color: var(--teal);
    text-align: center; letter-spacing: 1px;
  }
  .contact-card .brand-name { margin-top: 28px; font-size: 20px; }
  .tagline { font-family: "Roboto Condensed", Arial, sans-serif; text-align: center; }
  .contact-card .tagline { margin-top: 14px; font-size: 10.5px; color: var(--ink); }
  .contact-lines {
    margin: 16px 0 0 70px; font-size: 8.6px; line-height: 11.5px;
    color: var(--ink); font-weight: 600; font-style: normal;
  }
  .contact-lines p { margin-bottom: 11px; }
  .cover-brand { position: absolute; left: 700px; top: 88px; width: 400px; }
  .cover-brand .brand-name { font-size: 26px; color: #cfeff5; }
  .cover-tagline { position: absolute; left: 700px; top: 150px; width: 400px; font-size: 14px; color: var(--white); }
</style>
</head>
<body>
<main class="spread">
  <svg class="backdrop" width="1200" height="776" viewBox="0 0 1200 776" aria-hidden="true">
    <defs>
      <pattern id="diagonal-stripes" width="22" height="22" patternUnits="userSpaceOnUse" patternTransform="rotate(-45)">
        <rect width="22" height="22" fill="#e4e4e8"/>
        <rect width="22" height="5" fill="#ffffff"/>
      </pattern>
      <linearGradient id="purple-fade" x1="0" y1="0" x2="1" y2="1">
        <stop offset="0" stop-color="#a05aa8"/>
        <stop offset="1" stop-color="#4f4fa6"/>
      </linearGradient>
      <linearGradient id="top-band-left" x1="0" x2="1">
        <stop offset="0" stop-color="#6f6cb8"/>
        <stop offset="1" stop-color="#b3add6"/>
      </linearGradient>
      <linearGradient id="cover-band" x1="0" x2="1">
        <stop offset="0" stop-color="#6a5fb2"/>
        <stop offset="0.5" stop-color="#9a52a8"/>
        <stop offset="1" stop-color="#5a4fa8"/>
      </linearGradient>
      <linearGradient id="teal-arrow" x1="0" x2="1">
        <stop offset="0" stop-color="#1f8ea8"/>
        <stop offset="1" stop-color="#3cb4c8"/>
      </linearGradient>
    </defs>
    <rect width="1200" height="776" fill="url(#diagonal-stripes)"/>
    <rect x="0" y="0" width="600" height="52" fill="url(#top-band-left)"/>
    <polygon points="600,370 600,776 195,776" fill="url(#purple-fade)"/>
    <polygon points="0,48 445,48 470,85 445,122 0,122" fill="url(#teal-arrow)"/>
    <polygon points="600,0 1200,0 1200,200 600,190" fill="url(#cover-band)"/>
    <path d="M600,192 H745 Q765,195 750,215 L600,380 Z" fill="#1e96ae"/>
    <polygon points="1200,400 1200,776 880,776" fill="url(#purple-fade)"/>
  </svg>

  <h2 class="banner-title">Custom Mugs Bagtafs Keychains Openers<br>Pens Phone Bookmarks Stationary</h2>

  <div class="product-sheet sheet-a">
    <div class="sheet-section"><div class="section-bar">Chic Cases for Phone</div><div class="section-photos tone-pink" role="img" aria-label="Monogrammed patterned phone cases"></div></div>
    <div class="sheet-section"><div class="section-bar">Chic Stationery</div><div class="section-photos tone-blue" role="img" aria-label="Monogrammed stationery cards"></div></div>
    <div class="sheet-section"><div class="section-bar">Chic Pens</div><div class="section-photos tone-lime" role="img" aria-label="Patterned personalised pens"></div></div>
    <div class="sheet-section"><div class="section-bar">Chic Bookmarks</div><div class="section-photos tone-mix" role="img" aria-label="Monogrammed bookmarks with ribbons"></div></div>
  </div>
  <div class="product-sheet sheet-b">
    <div class="sheet-section"><div class="section-bar">Chic Tumblers</div><div class="section-photos tone-blue" role="img" aria-label="Monogrammed tumblers with straws"></div></div>
    <div class="sheet-section"><div class="section-bar">Chic Travel Mugs</div><div class="section-photos tone-pink" role="img" aria-label="Patterned travel mugs"></div></div>
    <div class="sheet-section"><div class="section-bar">Chic Bag Tags</div><div class="section-photos tone-mix" role="img" aria-label="Monogrammed bag tags"></div></div>
    <div class="sheet-section"><div class="section-bar">Chic Key Chains &amp; Bottle Openers</div><div class="section-photos tone-lime" role="img" aria-label="Monogrammed key chains and bottle openers"></div></div>
  </div>

  <p class="caption">these are unique gift items that we custom print onsite and give to your guests at the event. they get to choose from a variety of colors and designs, no one will go home disappointed</p>

  <section class="contact-card">
    <div class="brand-name">Brightvale Works</div>
    <div class="tagline">CREATING MEMORABLE EVENTS FOR OVER 35 YEARS!</div>
    <address class="contact-lines">
      <p>4820 Larkmoor Ave.<br>Cleveland, OH 44110</p>
      <p>P: (216) 555-0148<br>F: (216) 555-0172<br>toll free (888) 555-0193</p>
      <p>Florida Office:<br>2275 Palmcrest Lane North<br>Coral Harbor, FL 33480<br>(888) 555-0193</p>
      <p>info@brightvaleworks.com<br>sales@brightvaleworks.com</p>
    </address>
  </section>

  <div class="cover-brand"><div class="brand-name">Brightvale Works</div></div>
  <div class="tagline cover-tagline">CREATING MEMORABLE EVENTS FOR OVER 35 YEARS!</div>

  <svg class="collage" width="1200" height="776" viewBox="0 0 1200 776">
    <defs>
      <clipPath id="arrow-shape">
        <path d="M775,195 H1050 Q1080,195 1080,225 V366 H1097 V564 H1145 Q1165,564 1152,580 L935,776 L718,580 Q705,564 725,564 H775 Z"/>
      </clipPath>
      <linearGradient id="g-space" x1="0" y1="0" x2="0" y2="1"><stop offset="0" stop-color="#1d2a4a"/><stop offset="1" stop-color="#a8683a"/></linearGradient>
      <linearGradient id="g-paris" x1="0" y1="0" x2="0" y2="1"><stop offset="0" stop-color="#3d6fb8"/><stop offset="1" stop-color="#7a6a55"/></linearGradient>
      <linearGradient id="g-tags" x1="0" y1="0" x2="1" y2="1"><stop offset="0" stop-color="#3a3a3a"/><stop offset="1" stop-color="#a5a5a5"/></linearGradient>
      <linearGradient id="g-ocean" x1="0" y1="0" x2="0" y2="1"><stop offset="0" stop-color="#1c5f95"/><stop offset="1" stop-color="#4aa6cf"/></linearGradient>
      <linearGradient id="g-dino" x1="0" y1="0" x2="1" y2="1"><stop offset="0" stop-color="#3e6a3a"/><stop offset="1" stop-color="#a86a3c"/></linearGradient>
    </defs>
    <g clip-path="url(#arrow-shape)">
      <rect x="775" y="195" width="305" height="170" fill="url(#g-space)" role="img" aria-label="Photo of two girls beside a planetary rover model in a space scene"/>
      <rect x="775" y="367" width="158" height="195" fill="url(#g-paris)" role="img" aria-label="Photo of a young man in front of the Eiffel Tower"/>
      <rect x="935" y="367" width="162" height="195" fill="url(#g-tags)" role="img" aria-label="Photo of engraved photo dog tags and pendants"/>
      <rect x="700" y="564" width="233" height="212" fill="url(#g-ocean)" role="img" aria-label="Photo of a girl pointing at a dolphin underwater"/>
      <rect x="935" y="564" width="230" height="212" fill="url(#g-dino)" role="img" aria-label="Photo of a boy beside a dinosaur head"/>
    </g>
  </svg>
</main>
</body>
</html>
```